Business Cards for Marco and Tobin

Design of business cards for two people with the recently created brand Valcor Mobile. Valcor Mobile wants to become a worldwide major player on the secondhand phone market. It gathers send hand phones from individuals, refurbish them and sell them throughout the world. It has a green impact (recycling) and we also contribute to social project in Africa (a percentage of our benefits are sent to build school, sport facilities, etc.

Target Market(s)

B2B - Marco and Tobin are in contact with distributors across Africa.

Industry/Entity Type

Wireless Communication

Contact Information for Business Card

Marco Feuillet
Head of Emerging Markets
Valcor Energy South Africa (Pty) Ltd
Kestrel Road 47
2031 Sandton - Johannesburg
South Africa
Tel: + 27 10 555 0148
Mobile : +27 82 55 104
Email : marco.feuillet@valcormobile.example
Skype: marco.feuillet
Web: www.valcormobile.example
 

Tobin Farrow
Head of Southern Africa
Kestrel Road 47
South Africa
Tel: + 27 10 555 0148
Mobile: +27 83 555 0276
Email: tobin.farrow@valcormobile.example
Skype: tobin.farrow
Web: www.valcormobile.example

Requirements
Must have
• The cards need to be "serious", trustable, with a worldwide presence.
Nice to have
• Some "green" / recycling touch would be nice but not necessary if in contradiction with the general design.

```html
<!DOCTYPE html>
<html lang="en">
<head>
<meta charset="utf-8">
<title>Valcor Mobile – Business Card</title>
<link rel="stylesheet" href="https://fonts.googleapis.com/css2?family=Roboto:wght@400;500;700&display=swap">
<style>
  :root {
    --stage: #2b2b2d;
    --navy: #0d3550;
    --navy-deep: #0a2a40;
    --ink: #10344d;
    --text: #1f2a33;
    --accent: #2f8fd0;
    --paper: #ffffff;
    --paper-shade: #e6e8ea;
    --deco: rgba(200, 205, 210, 0.35);
  }
  * { box-sizing: border-box; margin: 0; padding: 0; }
  html, body {
    width: 1200px; height: 900px; overflow: hidden;
    background: var(--stage);
    font-family: "Roboto", Arial, sans-serif;
  }
  .canvas { position: relative; width: 1200px; height: 900px; }

  .card {
    position: absolute;
    width: 630px; height: 360px;
    border-radius: 26px;
    overflow: hidden;
    box-shadow: 0 14px 30px rgba(0,0,0,0.45);
  }

  /* Front */
  .card--front {
    left: 200px; top: 70px;
    background: radial-gradient(ellipse at 40% 30%, var(--navy) 0%, var(--navy-deep) 100%);
    display: flex; align-items: center; justify-content: center;
  }
  .brand {
    display: flex; align-items: center; gap: 12px;
    font-weight: 700; letter-spacing: -0.5px;
  }
  .brand__dot { width: 18px; height: 18px; border-radius: 50%; background: var(--accent); }
  .card--front .brand__name { color: var(--paper); font-size: 34px; }

  /* Back */
  .card--back {
    left: 370px; top: 470px;
    background: linear-gradient(135deg, var(--paper) 0%, var(--paper) 55%, var(--paper-shade) 100%);
  }
  .card__decoration {
    position: absolute; left: 140px; top: 0; width: 330px; height: 360px;
    background: linear-gradient(160deg, var(--deco), rgba(220,224,228,0.1));
  }
  .card--back .brand {
    position: absolute; left: 40px; top: 205px;
  }
  .card--back .brand__name { color: var(--ink); font-size: 34px; }
  .divider {
    position: absolute; left: 320px; top: 50px;
    width: 2px; height: 250px; background: var(--ink);
  }
  .details {
    position: absolute; left: 342px; top: 48px; width: 280px;
    color: var(--text); font-size: 13.5px; line-height: 1.35;
  }
  .person__name { color: var(--accent); font-weight: 700; font-size: 14.5px; }
  .person__title { font-size: 14.5px; margin-bottom: 14px; }
  .contact { list-style: none; margin-bottom: 14px; }
  .contact li { display: flex; align-items: center; gap: 8px; white-space: nowrap; }
  .contact svg { width: 13px; height: 13px; flex: none; fill: var(--ink); }
  .address__company { font-weight: 700; }
</style>
</head>
<body>
<main class="canvas">

  <section class="card card--front" aria-label="Card front">
    <div class="brand">
      <span class="brand__dot"></span>
      <span class="brand__name">Valcor Mobile</span>
    </div>
  </section>

  <section class="card card--back" aria-label="Card back">
    <div class="card__decoration" role="img" aria-label="Faint outlines of smartphones in pale grey"></div>

    <div class="brand">
      <span class="brand__dot"></span>
      <span class="brand__name">Valcor Mobile</span>
    </div>

    <div class="divider"></div>

    <div class="details">
      <p class="person__name">Marco Feuillet</p>
      <p class="person__title">Head of Emerging Markets</p>

      <ul class="contact">
        <li>
          <svg viewBox="0 0 16 16"><path d="M2 6c0-2 2-3 6-3s6 1 6 3l-3 1-1-2H6L5 7 2 6zm2 2h8l1 5H3l1-5zm4 1.5a1.5 1.5 0 100 3 1.5 1.5 0 000-3z"/></svg>
          <span>+ 27 10 555 0148</span>
        </li>
        <li>
          <svg viewBox="0 0 16 16"><path d="M4 1h8v14H4V1zm1.5 1.5v9h5v-9h-5zM8 12.5a.8.8 0 100 1.6.8.8 0 000-1.6z"/></svg>
          <span>+27 82 55 104</span>
        </li>
        <li>
          <svg viewBox="0 0 16 16"><path d="M1 3h14v10H1V3zm1 1l6 5 6-5H2z"/></svg>
          <span>marco.feuillet@valcormobile.example</span>
        </li>
        <li>
          <svg viewBox="0 0 16 16"><circle cx="8" cy="8" r="7"/></svg>
          <span>marco.feuillet</span>
        </li>
        <li>
          <svg viewBox="0 0 16 16"><path d="M8 1a7 7 0 100 14A7 7 0 008 1zm0 1.3c.8.8 1.4 2.1 1.6 3.7H6.4C6.6 4.4 7.2 3.1 8 2.3zM2.4 7h2.8c0 .7 0 1.4.1 2H2.4a5.7 5.7 0 010-2zm4 0h3.2v2H6.4V7zm4.4 0h2.8a5.7 5.7 0 010 2h-2.8c.1-.6.1-1.3 0-2zM6.4 10h3.2c-.2 1.6-.8 2.9-1.6 3.7-.8-.8-1.4-2.1-1.6-3.7z"/></svg>
          <span>www.valcormobile.example</span>
        </li>
      </ul>

      <address class="address" style="font-style: normal;">
        <p class="address__company">Valcor Energy South Africa (Pty) Ltd</p>
        <p>Kestrel Road 47</p>
        <p>2031 Sandton - Johannesburg</p>
        <p>South Africa</p>
      </address>
    </div>
  </section>

</main>
</body>
</html>
```